Exklusives Modernes Logo & Visitenkarte Design für Fotografie
Zielgruppe
Fine Art Photography, suche ein exklusives Design. Zielgruppe primär Privatpersonen, gehobene Gesellschaft.
Aufgabenstellung
Sehr hochwertiges Design! Für anspruchsvolle Kunden.
Visitenkarten Design außergewöhnlich bitte!
Vielleicht auch Guerilla-Marketing (Design)
Font: Miso & Jura
Für Visitenkarte:
Wendholm Fine Art Photography
Business Owner
Jonas Emil Wendholm
Office: Birkweg 14, 3651 Oberfelden on the Danube, Austria
Photoatelier: Neuer Platz 9, 3241 Grubau, Austria
Web: jonas-wendholm.example / E-Mail: mail@jonas-wendholm.example
Mobile +43(0) 660 17 38 904 - Austria
Fon: +43 (0) 2758 41 836 - Austria / +46 8 739 215 - Sweden
Fax: +43 (0) 2758 41 836 11

```html
<!DOCTYPE html>
<html lang="en">
<head>
<meta charset="utf-8">
<title>Wendholm Fine Art Photography – Business Card</title>
<link href="https://fonts.googleapis.com/css2?family=Jura:wght@500;700&family=Oswald:wght@500;600&family=Roboto:wght@400;500;700&display=swap" rel="stylesheet">
<style>
  :root {
    --stage: #232323;
    --ink: #0d0d0d;
    --paper: #ffffff;
    --text: #1a1a1a;
    --muted: #444444;
    --accent: #e3121b;
    --photo-dark: #060606;
    --photo-mid: #2a2622;
  }
  * { box-sizing: border-box; margin: 0; padding: 0; }
  html, body { width: 1200px; height: 780px; overflow: hidden; }
  body {
    background: var(--stage);
    display: flex; align-items: center; justify-content: center; gap: 40px;
    font-family: "Roboto", Arial, sans-serif;
  }
  .card {
    position: relative; width: 540px; height: 330px;
    border-radius: 22px; overflow: hidden;
  }
  /* Front */
  .card--front { background: var(--ink); color: var(--paper); }
  .front__photo {
    position: absolute; left: 90px; top: 0; width: 260px; height: 330px;
    background: radial-gradient(ellipse at 50% 45%, var(--photo-mid) 0%, var(--photo-dark) 70%, transparent 100%);
    opacity: .85;
  }
  .frame-corners { position: absolute; inset: 0; }
  .front__name {
    position: absolute; font-family: "Jura", sans-serif; font-weight: 700;
    font-size: 40px; letter-spacing: 7px; line-height: 1;
  }
  .front__name--first { left: 70px; top: 112px; }
  .front__name--last { right: 62px; top: 180px; }
  /* Back */
  .card--back { background: var(--paper); color: var(--text); display: flex; }
  .band {
    position: relative; width: 128px; flex: none; background: var(--ink); color: var(--paper);
  }
  .band__dot {
    position: absolute; top: 22px; left: 50%; margin-left: -9px;
    width: 18px; height: 18px; border-radius: 50%; background: var(--accent);
  }
  .band__mark {
    position: absolute; left: 0; right: 0; top: 60px; bottom: 20px;
    display: flex; align-items: center; justify-content: center;
  }
  .band__name {
    transform: rotate(-90deg); white-space: nowrap;
    font-family: "Jura", sans-serif; font-weight: 500; font-size: 20px;
    letter-spacing: 5px; line-height: 1.3;
  }
  .band__name span { display: block; }
  .back__body { position: relative; flex: 1; padding: 30px 26px 0 30px; }
  .brand__title {
    font-family: "Oswald", sans-serif; font-weight: 600; font-size: 27px;
    letter-spacing: .5px; line-height: 1; text-transform: uppercase;
  }
  .brand__sub {
    font-family: "Jura", sans-serif; font-size: 12px; letter-spacing: 9px;
    margin-top: 4px; color: var(--muted);
  }
  .person { margin-top: 26px; }
  .person__name { font-weight: 700; font-size: 13px; }
  .person__role { font-size: 12px; color: var(--muted); margin-top: 2px; }
  .contact { list-style: none; margin-top: 10px; font-size: 10px; line-height: 1.35; }
  .contact li { display: flex; gap: 8px; margin-bottom: 4px; }
  .contact svg { flex: none; margin-top: 1px; }
  .viewfinder { position: absolute; right: 26px; top: 126px; }
  .address {
    position: absolute; right: 24px; bottom: 44px; width: 184px;
    font-size: 9.5px; line-height: 1.4; color: var(--text);
  }
  .address p + p { margin-top: 2px; }
  .web {
    position: absolute; left: 30px; bottom: 18px;
    font-family: "Jura", sans-serif; font-weight: 700; font-size: 11px; letter-spacing: 1.5px;
    text-transform: uppercase;
  }
</style>
</head>
<body>

<section class="card card--front" aria-label="Business card, front">
  <div class="front__photo" role="img" aria-label="Dark moody portrait photograph of a photographer holding a camera"></div>
  <svg class="frame-corners" width="540" height="330" viewBox="0 0 540 330" aria-hidden="true">
    <g fill="none" stroke="#fff" stroke-width="5">
      <polyline points="30,52 30,30 52,30"/>
      <polyline points="488,30 510,30 510,52"/>
      <polyline points="30,278 30,300 52,300"/>
      <polyline points="488,300 510,300 510,278"/>
    </g>
  </svg>
  <div class="front__name front__name--first">JONAS</div>
  <div class="front__name front__name--last">WENDHOLM</div>
</section>

<section class="card card--back" aria-label="Business card, back">
  <aside class="band">
    <span class="band__dot"></span>
    <div class="band__mark">
      <div class="band__name"><span>WENDHOLM</span><span>FINE ART</span></div>
    </div>
  </aside>
  <div class="back__body">
    <div class="brand">
      <div class="brand__title">Wendholm Fine Art</div>
      <div class="brand__sub">PHOTOGRAPHY</div>
    </div>
    <div class="person">
      <div class="person__name">Jonas Emil Wendholm</div>
      <div class="person__role">Business Owner</div>
    </div>
    <ul class="contact">
      <li>
        <svg width="9" height="12" viewBox="0 0 9 12" aria-label="Mobile"><rect x="1" y=".5" width="7" height="11" rx="1.2" fill="none" stroke="#1a1a1a"/></svg>
        <span>+43(0) 660 17 38 904 - Austria</span>
      </li>
      <li>
        <svg width="9" height="12" viewBox="0 0 10 12" aria-label="Phone"><path d="M2 1 L4 1 L4.5 3.5 L3.2 4.5 Q4.3 7.3 6.5 8.6 L7.5 7.4 L9.5 8.2 L9.3 10.4 Q4 11 1.3 3 Z" fill="#1a1a1a"/></svg>
        <span>+43 (0) 2758 41 836 - Austria<br>+46 8 739 215 - Sweden</span>
      </li>
      <li>
        <svg width="9" height="12" viewBox="0 0 10 12" aria-label="Fax"><rect x="0" y="4" width="10" height="7" fill="#1a1a1a"/><rect x="2.5" y="0" width="5" height="5" fill="#1a1a1a"/></svg>
        <span>+43 (0) 2758 41 836 - Austria<br>+46 8 739 215 - Sweden</span>
      </li>
    </ul>
    <svg class="viewfinder" width="160" height="54" viewBox="0 0 160 54" aria-hidden="true">
      <g fill="none" stroke="#111" stroke-width="4">
        <polyline points="4,30 4,50 24,50"/>
        <polyline points="136,4 156,4 156,24"/>
      </g>
    </svg>
    <div class="address">
      <p>Office: Birkweg 14, 3651 Oberfelden on the Danube, Austria</p>
      <p>Photoatelier: Neuer Platz 9, 3241 Grubau, Austria</p>
      <p>E-Mail: mail@jonas-wendholm.example</p>
    </div>
    <div class="web">www.jonas-wendholm.example</div>
  </div>
</section>

</body>
</html>
```